Ridgeline Wild Craft DL flyer

I'm looking for a new flyer for my startup business. In Darwin Australia.
Aimed at family's and short stay tourists the "Ridgeline Wild Craft" 4 hr tour will give people a basic understanding of some essential bush survival skills in the Australian Outback.
things covered in this 4 hr tour are
1. Finding water.
2. finding food.
3. Finding/making shelter and fire.
4. Finding your way home.

The tour will pick clients up in an air conditioned purpose build 4WD and take them to a nearby bushland area where they will have the opportunity to catch and harvest some native bushtucker.
They will then be able to find/harvest some water for survival situations.
While we cook our bush tucker they will also learn to find their way home through ancient navigation techniques as well.

Clients will then be dropped back to their accomodation with some fun and vital knowledge of surviving in the Australian outback.
At the end of the tour the group will be able to take home a basic survival kit which they will be able to use through the skills they just gained on the tour.

I'd like a two sided DL size flyer emphasising the following points.
4hr/half day tour
Fun for the family
Free survival kit included.
Eat what you catch
Learn essential survival skills
Provided buy an experienced and passionate bushman.
$150/head including transfers.

I'll provide some pictures for the flyer and any extra content you require.

Target Market(s)

Family's
Short stay tourists

Industry/Entity Type

Tourism

Colors

Designer to choose colors to be used in the design.

Requirements
Must have
• As per brief
Nice to have
• Any extra content and flair designers would like to add
Should not have
• Any images which aren't Australian

```html
<!DOCTYPE html>
<html lang="en">
<head>
<meta charset="utf-8">
<title>Ridgeline Wild Craft – DL Flyer</title>
<link rel="stylesheet" href="https://fonts.googleapis.com/css2?family=Cinzel:wght@400;700&family=Crimson+Text:wght@400;600&family=Share+Tech+Mono&display=swap">
<style>
  :root{
    --olive:#9a9b38;
    --olive-dark:#6b6a2a;
    --ink:#1d1a14;
    --orange:#e8552a;
    --parchment-light:#f8f0d6;
    --parchment-dark:#d8b277;
    --white:#ffffff;
    --backdrop:#efeae2;
  }
  *{box-sizing:border-box;margin:0;padding:0}
  html,body{width:1069px;height:1200px;overflow:hidden;background:var(--backdrop)}
  .canvas{position:relative;width:1069px;height:1200px}
  .flyer{position:absolute;width:413px;height:865px;overflow:hidden;
    background:radial-gradient(ellipse at 50% 55%,var(--parchment-light) 0%,#f1e2bb 55%,var(--parchment-dark) 100%);
    box-shadow:0 6px 16px rgba(0,0,0,.25)}
  .flyer--front{left:84px;top:136px}
  .flyer--back{left:570px;top:232px}
  .abs{position:absolute}
  .photo-fill{position:absolute;display:block}
  .tilted-photo{position:absolute;background:var(--white);padding:7px;box-shadow:0 3px 8px rgba(0,0,0,.35)}
  .tilted-photo div{width:100%;height:100%}
  .round-photo{position:absolute;left:19px;top:256px;width:136px;height:136px;border-radius:50%;
    border:5px solid var(--white);background:radial-gradient(circle at 45% 45%,#a8b35a,#6d7a3a 55%,#d7c0a0);box-shadow:0 2px 6px rgba(0,0,0,.3)}
  .title{position:absolute;right:18px;font-family:'Cinzel',serif;text-align:right;line-height:1}
  .title__top{top:352px;font-size:40px;color:var(--olive-dark)}
  .title__main{top:420px;font-size:58px;color:var(--olive-dark);font-weight:700}
  .title__main .dark{color:var(--ink)}
  .title-rule{position:absolute;left:20px;right:20px;top:483px;height:1px;background:#b8a57a}
  .mono{font-family:'Share Tech Mono',monospace;color:var(--orange)}
  .tagline{position:absolute;left:0;right:0;top:500px;text-align:center;font-size:17px;letter-spacing:1.6px;line-height:24px}
  .features{position:absolute;left:22px;top:575px;list-style:none;font-family:'Crimson Text',serif;font-size:18px;color:var(--ink)}
  .features li{display:flex;align-items:center;height:32.5px}
  .features svg{width:19px;height:19px;margin-right:9px;flex:none}
  .price{position:absolute;font-size:15px;letter-spacing:1.2px;line-height:21px;text-align:center}
  .book-band{position:absolute;left:0;right:0;bottom:0;height:92px}
  .book-band svg{position:absolute;left:0;top:0;width:100%;height:20px}
  .book-band__fill{position:absolute;left:0;right:0;top:14px;bottom:0;background:var(--olive)}
  .book-band__cta{position:absolute;left:0;right:0;top:27px;text-align:center;font-family:'Cinzel',serif;font-weight:700;font-size:21px;color:var(--white)}
  .book-band__url{position:absolute;left:0;right:0;top:57px;text-align:center;font-family:'Share Tech Mono',monospace;font-size:17px;letter-spacing:2px;color:var(--white)}
  .top-band{position:absolute;left:0;right:0;top:0;height:52px;background:var(--olive)}
  .headline{position:absolute;left:0;right:0;top:168px;text-align:center;font-family:'Cinzel',serif;font-weight:700;font-size:43px;line-height:52px;color:var(--white);text-shadow:0 2px 4px rgba(0,0,0,.5)}
  .intro{position:absolute;left:18px;right:18px;top:336px;text-align:center;font-family:'Crimson Text',serif;font-size:17.5px;line-height:26px;color:var(--orange)}
  .topics{position:absolute;left:22px;top:490px;list-style:none;font-family:'Crimson Text',serif;font-size:19px;color:var(--ink);width:210px}
  .topics li{display:flex;line-height:27px;margin-bottom:10px}
  .topics .num{width:24px;flex:none;font-family:'Cinzel',serif;font-weight:700;font-size:22px;color:var(--olive-dark)}
</style>
</head>
<body>
<main class="canvas">

  <!-- Front side -->
  <section class="flyer flyer--front" aria-label="Flyer front">
    <svg class="photo-fill" style="left:0;top:0" width="413" height="330" viewBox="0 0 413 330" role="img" aria-label="Photo of a family in bush hats kneeling in the bushland learning to make fire">
      <defs>
        <linearGradient id="bushScene" x1="0" y1="0" x2="0" y2="1">
          <stop offset="0" stop-color="#4f6a3a"/>
          <stop offset=".5" stop-color="#7b7658"/>
          <stop offset="1" stop-color="#9a8a70"/>
        </linearGradient>
      </defs>
      <path d="M0 0H413V296Q230 330 0 262Z" fill="url(#bushScene)"/>
      <path d="M0 262Q230 330 413 296" fill="none" stroke="#fff" stroke-width="6"/>
    </svg>
    <div class="round-photo" role="img" aria-label="Photo of native bush fruit held in a hand"></div>

    <h1>
      <span class="title title__top">RIDGELINE</span>
      <span class="title title__main"><span class="dark">WILD</span> CRAFT</span>
    </h1>
    <div class="title-rule"></div>
    <p class="tagline mono">Provided buy an experienced and<br>passionate bushman.</p>

    <ul class="features">
      <li><svg viewBox="0 0 20 20"><rect x="1.5" y="3.5" width="14" height="14" fill="none" stroke="#6b6a2a" stroke-width="1.8"/><path d="M5 10l4 4 9-11" fill="none" stroke="#6b6a2a" stroke-width="2.4"/></svg>4hr/half day tour.</li>
      <li><svg viewBox="0 0 20 20"><rect x="1.5" y="3.5" width="14" height="14" fill="none" stroke="#6b6a2a" stroke-width="1.8"/><path d="M5 10l4 4 9-11" fill="none" stroke="#6b6a2a" stroke-width="2.4"/></svg>Free survival kit included.</li>
      <li><svg viewBox="0 0 20 20"><rect x="1.5" y="3.5" width="14" height="14" fill="none" stroke="#6b6a2a" stroke-width="1.8"/><path d="M5 10l4 4 9-11" fill="none" stroke="#6b6a2a" stroke-width="2.4"/></svg>Fun for the family!</li>
      <li><svg viewBox="0 0 20 20"><rect x="1.5" y="3.5" width="14" height="14" fill="none" stroke="#6b6a2a" stroke-width="1.8"/><path d="M5 10l4 4 9-11" fill="none" stroke="#6b6a2a" stroke-width="2.4"/></svg>Eat what you catch!</li>
      <li><svg viewBox="0 0 20 20"><rect x="1.5" y="3.5" width="14" height="14" fill="none" stroke="#6b6a2a" stroke-width="1.8"/><path d="M5 10l4 4 9-11" fill="none" stroke="#6b6a2a" stroke-width="2.4"/></svg>Learn essential survival skills!</li>
    </ul>

    <div class="tilted-photo" style="left:248px;top:578px;width:158px;height:140px;transform:rotate(8deg)">
      <div role="img" aria-label="Photo of pandanus palm leaves" style="background:linear-gradient(135deg,#3e5a30,#7d9a5a 50%,#4a3a25)"></div>
    </div>

    <p class="price mono" style="left:0;right:0;top:742px">$150/head including transfers.</p>

    <div class="book-band">
      <svg viewBox="0 0 413 20" preserveAspectRatio="none"><path d="M0 14L12 8 24 12 38 6 52 11 66 7 80 12 95 5 110 10 126 8 140 13 156 6 172 11 188 8 204 12 220 5 236 10 252 7 268 12 284 6 300 11 316 8 332 13 348 6 364 10 380 7 396 12 413 8V20H0Z" fill="#fff"/><path d="M0 17L14 12 28 15 42 10 58 14 74 11 90 15 106 9 122 13 138 11 154 15 170 10 186 14 202 11 218 15 234 9 250 13 266 11 282 15 298 10 314 14 330 11 346 15 362 10 378 13 394 11 413 14V20H0Z" fill="#9a9b38"/></svg>
      <div class="book-band__fill"></div>
      <p class="book-band__cta">BOOK NOW</p>
      <p class="book-band__url">www.RidgelineWildCraft.au</p>
    </div>
  </section>

  <!-- Back side -->
  <section class="flyer flyer--back" aria-label="Flyer back">
    <svg class="photo-fill" style="left:0;top:40px" width="413" height="290" viewBox="0 0 413 290" role="img" aria-label="Photo of a freshwater crayfish held in open hands">
      <defs>
        <linearGradient id="catchScene" x1="0" y1="0" x2="1" y2="1">
          <stop offset="0" stop-color="#8a7a6c"/>
          <stop offset=".5" stop-color="#b89a88"/>
          <stop offset="1" stop-color="#6a6a58"/>
        </linearGradient>
      </defs>
      <path d="M0 6L20 2 40 7 60 3 80 8 100 2 120 6 140 3 160 8 180 2 200 6 220 3 240 8 260 2 280 6 300 3 320 8 340 2 360 6 380 3 413 6V245Q250 300 0 232Z" fill="url(#catchScene)"/>
      <path d="M0 232Q250 300 413 245" fill="none" stroke="#fff" stroke-width="6"/>
    </svg>
    <div class="top-band"></div>
    <svg class="abs" style="left:0;top:40px" width="413" height="14" viewBox="0 0 413 14"><path d="M0 0H413V6L393 10 373 5 353 11 333 6 313 10 293 4 273 10 253 6 233 11 213 5 193 10 173 6 153 11 133 5 113 10 93 6 73 11 53 5 33 10 13 6 0 9Z" fill="#9a9b38"/></svg>

    <h2 class="headline">EAT WHAT<br>YOU CATCH!</h2>

    <p class="intro">Aimed at family's and short stay tourists the "Ridgeline Wild Craft" 4 hr tour will give people a basic understanding of some essential bush survival skills in the Australian Outback. things covered in this 4 hr tour are</p>

    <ol class="topics">
      <li><span class="num">1.</span><span>Finding water</span></li>
      <li><span class="num">2.</span><span>Finding food</span></li>
      <li><span class="num">3.</span><span>Finding/making shelter and fire.</span></li>
      <li><span class="num">4.</span><span>Finding your way home</span></li>
    </ol>

    <div class="tilted-photo" style="left:258px;top:474px;width:155px;height:140px;transform:rotate(10deg)">
      <div role="img" aria-label="Photo of sticks on the ground marking east and west" style="background:linear-gradient(160deg,#a08a6a,#c2a984 50%,#8c7458)"></div>
    </div>
    <div class="tilted-photo" style="left:232px;top:598px;width:170px;height:145px;transform:rotate(-8deg)">
      <div role="img" aria-label="Photo of the bushman guide in a wide-brim hat" style="background:linear-gradient(160deg,#7a8a5a,#b49a7a 55%,#5a5a48)"></div>
    </div>

    <p class="price mono" style="left:14px;width:200px;top:722px">$150/head including<br>transfers.</p>

    <div class="book-band">
      <svg viewBox="0 0 413 20" preserveAspectRatio="none"><path d="M0 14L12 8 24 12 38 6 52 11 66 7 80 12 95 5 110 10 126 8 140 13 156 6 172 11 188 8 204 12 220 5 236 10 252 7 268 12 284 6 300 11 316 8 332 13 348 6 364 10 380 7 396 12 413 8V20H0Z" fill="#fff"/><path d="M0 17L14 12 28 15 42 10 58 14 74 11 90 15 106 9 122 13 138 11 154 15 170 10 186 14 202 11 218 15 234 9 250 13 266 11 282 15 298 10 314 14 330 11 346 15 362 10 378 13 394 11 413 14V20H0Z" fill="#9a9b38"/></svg>
      <div class="book-band__fill"></div>
      <p class="book-band__cta">BOOK NOW</p>
      <p class="book-band__url">www.RidgelineWildCraft.au</p>
    </div>
  </section>

</main>
</body>
</html>
```